Business Card Design for Fashion Tech Startup

Dear designers, we need a business card for Asia's premier fashion tech startup.!

PebbleHop is discovery e-commerce destination for busy, discerning parents in Asia featuring leading independent designers of baby, kids fashion apparel and sustainable brands from around the world.

PebbleHop is a modern, contemporary fashion tech startup targeting well-educated, well travelled and affluent parents. We're NOT your typical kiddy store!! Our design philosophy & e-commerce site is more like Vask.com, Orimesa.com, Pondwick.com, Farthollow.com.
Updates

Hi, size of the business card should be 84mm X 55mm. Would appreciate some business card layouts in Portrait as added consideration, i fancy the idea of a Portrait business card. What's important is that the business card should pique the receiver's interest to log onto the website to learn more. Many thanks and love forward to the designs!

Target Market(s)

Though modern, classy in look, feel & positioning, PebbleHop does possess a cheeky, fun-loving personality as depicted by its logo and the segment it targets (baby, kids) though the key decision makers i.e primarily mums between 25-40 who are well educated/travelled, local & expatriates, internet/digitally savvy, mid-high income working mums.

Industry/Entity Type

E-Commerce

Requirements
Must have
• Name, designation, email, phone & mobile number.
Company url : www.pebblehop.sg
Slogan : Discovery e-commerce destination for discerning, busy parents
Nice to have
• Call to Action such as a Discount code offering 10% discount
or asking people to "Like" us on our Chatterly page/Chatterly URL

```html
<!DOCTYPE html>
<html lang="en">
<head>
<meta charset="utf-8">
<title>PebbleHop — Business Card, Front and Back</title>
<link rel="stylesheet" href="https://fonts.googleapis.com/css2?family=Oswald:wght@300;400&family=Pacifico&display=swap">
<style>
  :root {
    --stage: #2a2a2a;
    --card-white: #ffffff;
    --card-shadow: #b9b9b9;
    --sky: #d4e8f8;
    --sky-stripe: #cbe2f5;
    --navy: #3d5a73;
    --coral: #f0806a;
    --white: #ffffff;
  }
  * { margin: 0; padding: 0; box-sizing: border-box; }
  html, body { width: 1200px; height: 839px; overflow: hidden; background: var(--stage); }
  .board { position: relative; width: 1200px; height: 839px; font-family: "Oswald", sans-serif; }

  .card {
    position: absolute; top: 23px; width: 487px; height: 745px;
    background: var(--card-white);
    box-shadow: 8px 10px 0 var(--card-shadow);
  }
  .card--front { left: 53px; }
  .card--back { left: 634px; }

  .card__panel {
    position: absolute; left: 19px; top: 17px; right: 17px; bottom: 19px;
    border-radius: 16px; overflow: hidden;
    background: repeating-linear-gradient(90deg, var(--sky) 0 12px, var(--sky-stripe) 12px 24px);
  }
  .card--back .card__panel { left: 18px; right: 16px; }

  /* Front */
  .brand { position: absolute; left: 28px; top: 56px; display: flex; align-items: center; gap: 26px; }
  .brand__dot { width: 100px; height: 100px; border-radius: 50%; background: var(--coral); }
  .brand__name { font-size: 46px; font-weight: 400; color: var(--navy); line-height: 1; }

  .holder-name {
    position: absolute; left: 50px; top: 250px;
    font-size: 50px; font-weight: 400; color: var(--navy); line-height: 1; letter-spacing: 0.3px;
  }

  .contact-tab {
    position: absolute; left: 0; top: 321px; width: 43px; height: 192px;
    background: var(--coral); border-radius: 0 8px 8px 0;
  }
  .contact-tab::after {
    content: ""; position: absolute; inset: 4px 4px 4px -2px;
    border: 1.5px dashed var(--white); border-left: none; border-radius: 0 6px 6px 0;
  }
  .contact-tab svg { position: absolute; left: 11px; width: 20px; height: 20px; }

  .contact-list { position: absolute; left: 51px; top: 330px; list-style: none; }
  .contact-list li {
    position: absolute; left: 0; white-space: nowrap;
    font-size: 22px; font-weight: 300; color: var(--navy); line-height: 1;
  }

  .corner-mark {
    position: absolute; right: -70px; bottom: -90px; width: 300px; height: 300px;
    border-radius: 50%; background: var(--navy); opacity: 0.15;
  }

  /* Back */
  .bubble { position: absolute; left: 0; top: 0; width: 452px; height: 470px; }
  .bubble__art-label {
    position: absolute; left: 0; width: 452px; top: 283px; text-align: center;
    font-size: 30px; font-weight: 400; color: var(--coral); line-height: 1;
  }
  .tagline {
    position: absolute; left: 0; width: 452px; top: 462px; text-align: center;
    font-size: 22px; font-weight: 300; color: var(--navy); line-height: 29px;
  }
  .cta-lead {
    position: absolute; left: 0; width: 452px; top: 558px; text-align: center;
    font-family: "Pacifico", cursive; font-size: 24px; color: var(--navy); line-height: 1.3;
  }
  .cta-link {
    position: absolute; left: 84px; top: 609px; width: 283px; height: 42px;
    background: var(--coral); border-radius: 8px;
    font-size: 20px; font-weight: 300; color: var(--white);
    display: flex; align-items: center; justify-content: center;
  }

  .side-label {
    position: absolute; top: 796px; width: 200px; text-align: center;
    font-size: 25px; font-weight: 300; color: var(--white); letter-spacing: 0.5px;
  }
  .side-label--front { left: 197px; }
  .side-label--back { left: 817px; }
</style>
</head>
<body>
<main class="board">

  <section class="card card--front" aria-label="Front of card">
    <div class="card__panel">
      <div class="corner-mark" aria-hidden="true"></div>

      <div class="brand">
        <span class="brand__dot" aria-hidden="true"></span>
        <span class="brand__name">PebbleHop</span>
      </div>

      <h1 class="holder-name">Maren T. Ellison</h1>

      <div class="contact-tab" aria-hidden="true">
        <svg style="top:19px" viewBox="0 0 20 20" fill="none" stroke="#fff" stroke-width="1.5">
          <rect x="2" y="5" width="16" height="11"/><path d="M2 5l8 6 8-6"/>
        </svg>
        <svg style="top:58px" viewBox="0 0 20 20" fill="none" stroke="#fff" stroke-width="1.5">
          <rect x="6" y="2" width="8" height="16" rx="1.5"/><path d="M9 15h2"/>
        </svg>
        <svg style="top:106px" viewBox="0 0 20 20">
          <rect x="2" y="2" width="16" height="16" rx="3" fill="#fff"/>
          <path d="M7 5c-1 1-1 3 0 5s3 4 5 5c1 .5 2 0 2.5-.5l-2-2-1.3.7c-1-.6-2.2-1.8-2.8-2.8L9 9 7 5z" fill="#f0806a"/>
        </svg>
        <svg style="top:154px" viewBox="0 0 20 20" fill="none" stroke="#fff" stroke-width="1.3">
          <circle cx="10" cy="10" r="8"/><ellipse cx="10" cy="10" rx="3.5" ry="8"/><path d="M2 10h16M3.5 6h13M3.5 14h13"/>
        </svg>
      </div>

      <ul class="contact-list">
        <li style="top:0">MarenTEllison@mailbay.com</li>
        <li style="top:42px">555-204-7381</li>
        <li style="top:91px">5550193846</li>
        <li style="top:138px">www.pebblehop.sg</li>
      </ul>
    </div>
  </section>

  <section class="card card--back" aria-label="Back of card">
    <div class="card__panel">
      <svg class="bubble" viewBox="0 0 452 470" aria-hidden="true">
        <defs>
          <radialGradient id="art-tone" cx="50%" cy="50%" r="50%">
            <stop offset="0" stop-color="#ffffff"/>
            <stop offset="0.45" stop-color="#f7d4cb"/>
            <stop offset="1" stop-color="#c9d3dd"/>
          </radialGradient>
        </defs>
        <circle cx="221" cy="221" r="190" fill="none" stroke="#fff" stroke-width="1.2" stroke-dasharray="3 3"/>
        <path d="M221 40a181 181 0 0 1 60 351.8L226 448q-5 5 -10 0L161 391.8A181 181 0 0 1 221 40z" fill="#fff"/>
      </svg>
      <svg class="bubble" viewBox="0 0 452 470" role="img" aria-label="Circular cluster of baby and kids item illustrations: clothes, toys, bottles, prams and rocking horse">
        <circle cx="221" cy="218" r="165" fill="url(#art-tone)"/>
      </svg>
      <div class="bubble__art-label">PebbleHop.sg</div>

      <p class="tagline">Discovery e-commerce destination<br>for discerning, busy parents</p>
      <p class="cta-lead">Find more about us here:</p>
      <div class="cta-link">http://www.chatterly/pebblehop</div>
    </div>
  </section>

  <div class="side-label side-label--front">FRONTSIDE</div>
  <div class="side-label side-label--back">BACKSIDE</div>

</main>
</body>
</html>
```